I need this design by August 8th or 9th!
Looking for a classy, but FUn door hangers for a community outreach "Harvest Fun Jamboree." While we are a faith-based organization, we do NOT want this to look religious. I put the LP square blue so you would have a color reference. With grey and orange as an accent color.
Event: Harvest Fun Jamboree!
Location: Calloway Meadow Estates neighborhood pavilion by the red silo.
Date: Friday, August 17th
Time: 5:30 p.m. to 8:30 p.m.
Free food, while supplies last!
Yummy desserts,
Bounce house,
Raffle,
Games and activities.

Target Market(s)

Families in the neighborhood

Colors
acd136
959595
fbee3d

Requirements
Must have
• Door hanger,

```html
<!DOCTYPE html>
<html lang="en">
<head>
<meta charset="utf-8">
<title>Harvest Fun Jamboree – Door Hanger</title>
<link rel="stylesheet" href="https://fonts.googleapis.com/css2?family=Bangers&family=Comic+Neue:wght@700&family=Allura&display=swap">
<style>
  :root {
    --stage: #c9c8c8;
    --bleed: #ffffff;
    --slate: #8b96a9;
    --frame: #ffffff;
    --yellow: #f6ec32;
    --green: #a6cd3a;
    --ink: #111111;
    --brand-blue: #4a7089;
    --white: #ffffff;
  }
  * { box-sizing: border-box; margin: 0; padding: 0; }
  html, body {
    width: 1200px; height: 2250px; overflow: hidden;
    background: var(--stage);
  }
  .canvas { position: relative; width: 1200px; height: 2250px; }
  .bleed {
    position: absolute; left: 168px; top: 140px; width: 864px; height: 1970px;
    background: var(--bleed);
  }
  .hanger {
    position: absolute; left: 185px; top: 156px; width: 831px; height: 1937px;
    background: var(--slate); overflow: hidden;
  }
  .doodle-field {
    position: absolute; inset: 0;
    background: linear-gradient(170deg, #8e99ac 0%, #8893a6 60%, #8a95a8 100%);
  }
  .shapes { position: absolute; inset: 0; }
  .pencils {
    position: absolute; left: 0; bottom: 0; width: 831px; height: 280px;
    background: linear-gradient(90deg, #7f9a3c 0%, #5aa64e 14%, #3ea0a0 28%, #2f8fc9 40%, #2d4f98 54%, #4c3d8e 66%, #7c3f8a 78%, #b8357e 90%, #c42f78 100%);
  }
  .title {
    position: absolute; left: 0; width: 831px; top: 505px;
    text-align: center;
    font-family: "Bangers", "Comic Neue", sans-serif; font-weight: 400;
    font-size: 130px; line-height: 122px; letter-spacing: 2px;
    color: var(--white);
    text-shadow: 6px 6px 0 var(--ink);
    transform: rotate(-5deg);
  }
  .pill {
    position: absolute; display: flex; align-items: center; gap: 22px;
    font-family: "Comic Neue", "Comic Sans MS", sans-serif; font-weight: 700;
    font-size: 31px; line-height: 1.2; color: var(--ink);
    white-space: nowrap;
  }
  .pill--yellow { background: var(--yellow); }
  .pill--green { background: var(--green); }
  .pill--info {
    left: -20px; padding-left: 75px; border-radius: 0 55px 55px 0;
    transform: rotate(-3deg); transform-origin: left center;
  }
  .pill--feature {
    right: -30px; justify-content: flex-end; padding-right: 80px;
    border-radius: 40px 0 0 40px;
    transform: rotate(-3deg); transform-origin: right center;
  }
  .pill-icon { width: 38px; height: 38px; flex: none; }
  .brand {
    position: absolute; left: 67px; top: 1674px; width: 195px; height: 195px;
    background: var(--brand-blue); border: 4px solid var(--white); border-radius: 18px;
    display: flex; align-items: center; justify-content: center;
    font-family: "Comic Neue", "Comic Sans MS", sans-serif; font-weight: 700;
    font-size: 90px; color: var(--white);
  }
  .hashtag {
    position: absolute; left: 415px; top: 1765px;
    font-family: "Allura", cursive; font-size: 62px; line-height: 1;
    color: var(--white); white-space: nowrap;
    transform: rotate(-4deg);
  }
  .crop-marks { position: absolute; inset: 0; }
</style>
</head>
<body>
<div class="canvas">
  <div class="bleed"></div>
  <div class="hanger">
    <div class="doodle-field" role="img" aria-label="Line-drawn school supply doodles on ruled paper in teal and slate"></div>

    <svg class="shapes" width="831" height="1937" viewBox="0 0 831 1937">
      <rect class="inner-frame" x="60" y="60" width="711" height="1620" fill="none" stroke="#ffffff" stroke-width="3"/>
      <polygon class="hanger-slot" points="115,-10 185,-10 420,260 360,330" fill="#ffffff"/>
      <circle class="hanger-ring" cx="377" cy="295" r="155" fill="#8b96a9" stroke="#ffffff" stroke-width="3"/>
      <circle class="hanger-hole" cx="377" cy="295" r="130" fill="#ffffff"/>
    </svg>

    <div class="pencils" role="img" aria-label="Row of colored pencils in a rainbow of greens, blues, purples and pinks"></div>

    <h1 class="title">Harvest<br>Fun<br>Jamboree!</h1>

    <div class="pill pill--yellow pill--info" style="top:984px;width:728px;height:105px;">
      <svg class="pill-icon" viewBox="0 0 24 24" fill="none" stroke="#111" stroke-width="1.6"><path d="M12 21s-6-6.2-6-11a6 6 0 0 1 12 0c0 4.8-6 11-6 11z"/><circle cx="12" cy="10" r="2.2"/><path d="M7 21h10"/></svg>
      <span>Calloway Meadow Estates neighborhood<br>pavilion by the red silo.</span>
    </div>
    <div class="pill pill--green pill--info" style="top:1101px;width:510px;height:72px;">
      <svg class="pill-icon" viewBox="0 0 24 24" fill="none" stroke="#111" stroke-width="1.6"><rect x="3" y="5" width="18" height="16" rx="1.5"/><path d="M3 9h18M8 3v4M16 3v4"/><path d="M13 16l2 2 4-4"/></svg>
      <span>Friday, August 17th</span>
    </div>
    <div class="pill pill--yellow pill--info" style="top:1182px;width:600px;height:74px;">
      <svg class="pill-icon" viewBox="0 0 24 24" fill="none" stroke="#111" stroke-width="1.6"><circle cx="12" cy="12" r="9"/><path d="M12 7v5l3 2"/></svg>
      <span>5:30 p.m. to 8:30 p.m.</span>
    </div>

    <div class="pill pill--green pill--feature" style="top:1298px;width:697px;height:72px;">Free food while supplies last!</div>
    <div class="pill pill--yellow pill--feature" style="top:1368px;width:550px;height:72px;">Bounce house</div>
    <div class="pill pill--green pill--feature" style="top:1440px;width:633px;height:72px;">Yummy desserts</div>
    <div class="pill pill--yellow pill--feature" style="top:1514px;width:517px;height:72px;">Raffle</div>
    <div class="pill pill--green pill--feature" style="top:1593px;width:573px;height:72px;">Games and activities</div>

    <div class="brand">LP</div>
    <div class="hashtag">#ForBrookhaven</div>
  </div>

  <svg class="crop-marks" width="1200" height="2250" viewBox="0 0 1200 2250" stroke="#222" stroke-width="1.5" fill="none">
    <path d="M212 120v60M168 156h45"/>
    <path d="M988 120v60M988 156h45"/>
    <path d="M212 2070v60M168 2093h45"/>
    <path d="M988 2070v60M988 2093h45"/>
  </svg>
</div>
</body>
</html>
```